new private customer brochure

New brochure for advertising our services in bathroom remodeling, heating system renovation, and ventilation cleaning. Brochure size A5 with 4 pages. More informations about the company will you see on the website: www.talbrunex.ch

```html
<!DOCTYPE html>
<html lang="de">
<head>
<meta charset="utf-8">
<title>Talbrunex Broschüre – Titelseite</title>
<link href="https://fonts.googleapis.com/css2?family=Montserrat:wght@400;600;700;800&display=swap" rel="stylesheet">
<style>
  :root {
    --bg: #d9d8dc;
    --yellow: #f4ec13;
    --black: #0e0e0e;
    --white: #ffffff;
    --sky-top: #7fb2e4;
    --sky-low: #cfe2f4;
    --ink: #121212;
  }
  * { margin: 0; padding: 0; box-sizing: border-box; }
  html, body { width: 1200px; height: 840px; overflow: hidden; background: var(--bg); }
  body { font-family: "Montserrat", sans-serif; color: var(--ink); }

  .cover {
    position: absolute;
    left: 324px; top: 30px;
    width: 552px; height: 780px;
    overflow: hidden;
    box-shadow: 0 18px 40px rgba(0,0,0,0.18);
  }
  .cover__shapes { position: absolute; inset: 0; }

  .brand { position: absolute; left: 40px; top: 62px; }
  .brand__name {
    display: flex; align-items: center; gap: 10px;
    font-weight: 800; font-size: 40px; letter-spacing: 1px; line-height: 1;
  }
  .brand__dot { width: 26px; height: 26px; border-radius: 50%; background: var(--ink); }
  .brand__tag {
    margin-top: 8px; font-size: 11px; font-weight: 400; letter-spacing: 2.4px;
  }

  .services { position: absolute; left: 44px; top: 468px; }
  .services__title {
    font-weight: 800; font-size: 23px; line-height: 1.05; text-transform: uppercase;
  }
  .services__list { list-style: none; margin-top: 16px; }
  .services__item {
    display: flex; align-items: center; gap: 10px;
    font-weight: 700; font-size: 14px; margin-bottom: 9px;
  }
  .services__icon { width: 17px; height: 17px; border-radius: 50%; background: var(--ink); flex: none; }

  .contact {
    position: absolute; right: 22px; top: 460px;
    text-align: right; color: var(--white);
  }
  .contact__label { font-weight: 700; font-size: 14px; margin-bottom: 8px; }
  .contact__phone { font-weight: 700; font-size: 15px; }
  .contact__mail { font-weight: 400; font-size: 11px; margin-top: 2px; }
</style>
</head>
<body>
  <main class="cover">
    <svg class="cover__shapes" width="552" height="780" viewBox="0 0 552 780">
      <defs>
        <linearGradient id="photoTone" x1="0" y1="0" x2="0.4" y2="1">
          <stop offset="0" stop-color="var(--sky-top)"/>
          <stop offset="0.45" stop-color="var(--sky-low)"/>
          <stop offset="0.7" stop-color="#c9c9c4"/>
          <stop offset="1" stop-color="#4f6e3a"/>
        </linearGradient>
      </defs>
      <rect class="cover__photo" width="552" height="780" fill="url(#photoTone)" role="img" aria-label="Fotografie: Schnittmodell eines Einfamilienhauses mit Haustechnik vor blauem Himmel und Baum"/>
      <polygon class="cover__corner-top" points="320,0 552,0 552,100" fill="var(--black)"/>
      <polygon class="cover__band-top" points="0,0 330,0 40,165 0,165" fill="var(--yellow)"/>
      <polygon class="cover__band-contact" points="300,470 552,400 552,660" fill="var(--black)"/>
      <polygon class="cover__band-bottom" points="0,470 230,385 552,640 552,780 0,780" fill="var(--yellow)"/>
      <polygon class="cover__corner-bottom" points="0,735 150,700 330,780 0,780" fill="var(--black)"/>
    </svg>

    <div class="brand">
      <div class="brand__name"><span>TALBRUNEX</span><span class="brand__dot"></span></div>
      <div class="brand__tag">HAUSTECHNIK + BAUSPENGLEREI</div>
    </div>

    <section class="services">
      <h1 class="services__title">Talbrunex<br>Building Expertise</h1>
      <ul class="services__list">
        <li class="services__item"><span class="services__icon"></span>Heizungsersatz</li>
        <li class="services__item"><span class="services__icon"></span>Ersatz sanitäre Anlagen</li>
        <li class="services__item"><span class="services__icon"></span>Lüftungsanlagenersatz</li>
        <li class="services__item"><span class="services__icon"></span>Photovoltaik Anlagen</li>
        <li class="services__item"><span class="services__icon"></span>Dach- und Fassade</li>
      </ul>
    </section>

    <address class="contact" style="font-style: normal;">
      <div class="contact__label">Kontakt</div>
      <div class="contact__phone">Tel. 044 318 72 40</div>
      <div class="contact__mail">info@talbrunex.ch</div>
    </address>
  </main>
</body>
</html>
```